US Based Startup requires Website Design for Kavrelon Cell

We are launching a battery technology called "Kavrelon Cell" for which we need an elegant website design. We use red and black to represent positive and negative node color used in battery. The background is white. The font must provide more wide space and easy to read.
Kavrelon CellTM is a technology that uses fast switches, such as transistor switches, to make batteries more efficient. Orvane Technology can be implemented in all types of batteries – including non-rechargeable batteries, rechargeable batteries, wet-cell batteries and all metal oxide batteries.
Normal batteries are “non-switching”, that is, these batteries can only be connected to one another in parallel or series connections. Parallel connections enable batteries to charge faster whilst series connections enable the battery to discharge more efficiently to the load.
Kavrelon CellTM technology enables batteries to be connected in a third connection method called “vexa-loopTM” that combines the benefit of faster charging of the batteries with renewable energy source, such as solar, in parallel connection, and then quickly re-configures the same batteries using the fast transistor switches, to be connected in series with the load, to discharge efficiently.

Target Market(s)

Renewable energy

Industry/Entity Type

Renewable

Coding

Coded - Design and coding required

Number of Pages Required

5+ page

Requirements
Must have
• The primary colors are red and black for logo and fonts. The background is white.
The font must be easy to read type of fonts with more white space. Only pictures will be in full color.
Nice to have
• Elegant and simple design bringing out a new battery concept to the energy industry.

```html
<!DOCTYPE html>
<html lang="en">
<head>
<meta charset="utf-8">
<title>Orvane Technology — Kavrelon Cell</title>
<link href="https://fonts.googleapis.com/css2?family=Urbanist:wght@300;400;500;600;700;800;900&display=swap" rel="stylesheet">
<style>
:root{
  --red:#e41d2f;
  --black:#1f1f1f;
  --ink:#2b2b2b;
  --grey:#6b6b6b;
  --light:#f4f4f4;
  --pink:#fdf0f0;
  --dark:#232323;
  --white:#ffffff;
}
*{margin:0;padding:0;box-sizing:border-box}
html,body{width:1200px;height:4156px;overflow:hidden;background:var(--white)}
body{position:relative;font-family:"Urbanist",sans-serif;color:var(--ink)}
.abs{position:absolute}
.btn{position:absolute;background:var(--red);color:var(--white);font-weight:800;font-size:12px;letter-spacing:.5px;text-transform:uppercase;display:flex;align-items:center;justify-content:center;border-radius:3px}
.brand{font-weight:800;color:var(--red);font-size:20px;letter-spacing:1px;line-height:1.1}
p.body{font-size:12.5px;line-height:21px;color:var(--grey)}

/* header */
.site-header{left:0;top:0;width:1200px;height:77px;background:var(--white)}
.site-header .brand{left:184px;top:18px;width:170px}
.main-nav{left:432px;top:30px;display:flex;gap:32px;font-size:11.5px;font-weight:700;color:var(--black)}
.main-nav .active{position:relative}
.main-nav .active:after{content:"";position:absolute;left:3px;right:3px;top:22px;height:2px;background:var(--red)}
.call{left:880px;top:20px;display:flex;gap:12px;align-items:center}
.call .ico{width:36px;height:36px;border-radius:50%;background:var(--black);display:flex;align-items:center;justify-content:center}
.call small{display:block;font-size:11px;color:var(--grey);font-weight:600}
.call b{display:block;font-size:14px;color:var(--red);font-weight:800}

/* hero */
.hero{left:0;top:77px;width:1200px;height:650px;overflow:hidden}
.hero-photo{position:absolute;inset:0;background:linear-gradient(180deg,#7a7473 0%,#55504f 45%,#3a3838 100%)}
.hero-kicker{left:184px;top:160px;color:var(--white);font-size:22px;letter-spacing:12px;font-weight:400;line-height:26px;white-space:nowrap}
.hero-title{left:184px;top:196px;color:var(--white);font-size:72px;font-weight:900;line-height:76px;letter-spacing:1px;text-transform:uppercase;white-space:nowrap}
.arrow{position:absolute;width:56px;height:56px;border:2px solid var(--white);border-radius:50%;display:flex;align-items:center;justify-content:center}

/* about */
.about-visual{left:184px;top:830px;width:406px;height:406px;border-radius:50%;background:radial-gradient(circle at 45% 40%,#6c7ea2,#3b3f6a 60%,#1c2040)}
.kicker{font-size:16px;color:var(--grey);font-weight:500}
.h2{font-size:34px;font-weight:900;color:var(--black);line-height:38px;text-transform:uppercase}
.h2 span{font-weight:300}

/* why us */
.why-band{left:0;top:1365px;width:660px;height:517px;background:var(--pink)}
.why-vert{left:50px;top:1790px;transform:rotate(-90deg);transform-origin:left top;font-size:76px;font-weight:800;color:transparent;-webkit-text-stroke:1.5px #e9cfcf;letter-spacing:2px}
.why-photo{left:660px;top:1341px;width:540px;height:566px;border-radius:14px 0 0 14px;background:linear-gradient(120deg,#d9d7d3,#b9b6b0 60%,#8d8a85)}
.feature{position:absolute;left:182px;display:flex;gap:20px;width:380px}
.hex{width:66px;height:72px;flex:none;display:flex;align-items:center;justify-content:center}
.feature h4{font-size:14px;font-weight:700;color:var(--black);margin:3px 0 6px}
.feature p{font-size:12px;line-height:21px;color:var(--grey)}

/* services */
.center{left:0;width:1200px;text-align:center}
.card{position:absolute;top:2070px;width:191px;height:178px;border:1px solid #e7e7e7;border-radius:6px;box-shadow:0 4px 12px rgba(0,0,0,.06);display:flex;flex-direction:column;align-items:center;justify-content:flex-end;padding-bottom:40px;font-size:15px;font-weight:700;color:var(--black);gap:18px;background:var(--white)}
.card.featured{background:linear-gradient(180deg,#4a5248,#2f352f);color:var(--white);border:none}

/* projects */
.projects{left:0;top:2406px;width:1200px;height:580px}
.proj-vert{left:60px;top:2880px;transform:rotate(-90deg);transform-origin:left top;font-size:80px;font-weight:800;color:transparent;-webkit-text-stroke:1.5px #4a4a4a;letter-spacing:2px}
.proj-photo{left:185px;top:2478px;width:355px;height:382px;clip-path:polygon(25% 2%,75% 2%,100% 50%,75% 98%,25% 98%,0 50%);border-radius:30px;background:linear-gradient(140deg,#8c6f5a,#4c4039 50%,#2a2624)}
.badge{left:415px;top:2477px;width:100px;height:100px;border-radius:50%;background:var(--red);color:var(--white);text-align:center;padding-top:22px;line-height:1}
.badge b{font-size:28px;font-weight:900}
.badge small{font-size:11px;font-weight:700}
.badge div{font-size:13px;font-weight:600;margin-top:4px}
.dot{position:absolute;width:34px;height:34px;border-radius:50%;display:flex;align-items:center;justify-content:center}
.proj-text p{font-size:12.5px;line-height:21px;color:#e4e4e4;margin-bottom:14px}

/* testimonials */
.tcard{position:absolute;top:3150px;background:var(--white);box-shadow:0 3px 18px rgba(0,0,0,.07);text-align:center;padding:22px 22px 0}
.tcard .quote{position:absolute;left:32px;top:8px;font-size:90px;font-weight:900;color:#e6e6e6;line-height:1}
.tcard .stars{font-size:18px;color:#777;letter-spacing:3px;margin-left:70px;height:34px}
.tcard.mid .stars{color:var(--red)}
.tcard p{font-size:12.2px;line-height:21px;color:var(--grey)}
.tcard h5{font-size:13px;font-weight:800;color:var(--black);margin-top:24px;letter-spacing:.5px}
.tcard small{font-size:12px;color:var(--grey)}

/* cta */
.cta{left:0;top:3485px;width:1200px;height:350px;background:linear-gradient(180deg,#2d2a2a 0%,#4d2a22 55%,#6a2f24 100%)}
.cta h2{font-size:34px;font-weight:900;color:var(--white);line-height:38px}
.cta h2 span{font-weight:300}

/* footer */
.footer-col h6{font-size:12px;font-weight:800;color:var(--red);letter-spacing:.5px;margin-bottom:16px}
.footer-col li{list-style:none;font-size:12.5px;color:var(--ink);margin-bottom:10px}
.contact-row{display:flex;gap:10px;font-size:12px;color:var(--ink);margin-bottom:14px;line-height:15px}
.social{position:absolute;top:4017px;width:32px;height:32px;border:1px solid #bbb;border-radius:50%}
</style>
</head>
<body>

<!-- header -->
<header class="abs site-header">
  <div class="abs brand">ORVANE<br>TECHNOLOGY</div>
  <nav class="abs main-nav">
    <span class="active">HOME</span><span>ABOUT US</span><span>SERVICES</span><span>BLOG</span><span>CONTACT US</span>
  </nav>
  <div class="abs call">
    <div class="ico"><svg width="16" height="16" viewBox="0 0 24 24"><path fill="#fff" d="M6.6 10.8a15 15 0 0 0 6.6 6.6l2.2-2.2a1 1 0 0 1 1-.25 11.4 11.4 0 0 0 3.6.57 1 1 0 0 1 1 1V20a1 1 0 0 1-1 1A17 17 0 0 1 3 4a1 1 0 0 1 1-1h3.5a1 1 0 0 1 1 1c0 1.25.2 2.45.57 3.57a1 1 0 0 1-.25 1z"/></svg></div>
    <div><small>CALL US</small><b>555-014-2738</b></div>
  </div>
</header>

<!-- hero -->
<section class="abs hero">
  <div class="hero-photo" role="img" aria-label="Close-up of rows of industrial batteries with cables"></div>
  <div class="abs hero-kicker">RENEWABLE ENERGY</div>
  <h1 class="abs hero-title">Kavrelon<br>Cell</h1>
  <div class="btn" style="left:184px;top:370px;width:152px;height:43px">Contact Now</div>
  <div class="arrow" style="left:85px;top:243px"><svg width="14" height="14" viewBox="0 0 14 14"><path d="M9 2 4 7l5 5" stroke="#fff" stroke-width="2" fill="none"/></svg></div>
  <div class="arrow" style="left:1059px;top:243px"><svg width="14" height="14" viewBox="0 0 14 14"><path d="m5 2 5 5-5 5" stroke="#fff" stroke-width="2" fill="none"/></svg></div>
  <svg class="abs" style="left:0;top:470px" width="1200" height="180" viewBox="0 0 1200 180">
    <path d="M0 120 Q600 210 1200 60 L1200 180 L0 180Z" fill="#fff"/>
    <path d="M0 95 Q500 230 1200 60 Q600 190 0 150Z" fill="var(--red)"/>
    <path d="M0 70 Q300 150 560 165 Q250 150 0 95Z" fill="#1c1c1c"/>
  </svg>
</section>

<!-- about -->
<div class="abs about-visual" role="img" aria-label="Lightning bolt emblem filled with a photo of battery assembly"></div>
<div class="abs" style="left:660px;top:893px;width:360px">
  <div class="kicker">About <span style="display:inline-block;width:30px;height:1px;background:var(--red);vertical-align:middle;margin-left:6px"></span></div>
  <h2 class="h2" style="margin:6px 0 14px">The Company</h2>
  <p class="body">Lorem ipsum dolor sit amet, consectetur adipisicing elit, sed do eiusmod tempor incididunt ut labore et dolore magna aliqua. Ut enim ad minim veniam, quis nostrud exercitation ullamco laboris nisi ut aliquip ex ea commodo consequat. Duis aute irure dolor in reprehenderit in voluptate velit esse cillum dolore eu fugiat nulla pariatur. Excepteur sint occaecat cupidatat non proident, sunt in culpa qui officia deserunt mollit anim id est laborum. Sed ut perspiciatis.</p>
</div>
<div class="btn" style="left:660px;top:1159px;width:127px;height:41px;font-size:11px">More About Us</div>

<!-- why us -->
<div class="abs why-band"></div>
<div class="abs why-vert">WHY US</div>
<div class="abs why-photo" role="img" aria-label="Interior of a room with a newly installed battery enclosure wall"></div>
<h2 class="abs h2" style="left:184px;top:1410px">We Are Building<br><span>A Sustainable Future</span></h2>

<div class="feature" style="top:1515px">
  <svg class="hex" viewBox="0 0 66 72"><path d="M33 2 63 19v34L33 70 3 53V19Z" fill="var(--red)"/><circle cx="33" cy="36" r="15" fill="none" stroke="#fff" stroke-width="2.5"/><path d="M36 25 28 38h6l-3 10 8-14h-6z" fill="#fff"/></svg>
  <div><h4>Best Energy Solutions</h4><p>Lorem ipsum dolor sit amet, consectetur sed do adipiscing elit, sed do eiusmod tempor labore incididunt ut labore et dolore magna aliqua.</p></div>
</div>
<div class="feature" style="top:1631px">
  <svg class="hex" viewBox="0 0 66 72"><path d="M33 2 63 19v34L33 70 3 53V19Z" fill="var(--red)"/><circle cx="33" cy="36" r="11" fill="none" stroke="#fff" stroke-width="6" stroke-dasharray="4 3"/><circle cx="33" cy="36" r="5" fill="#fff"/></svg>
  <div><h4>End-To-End Services</h4><p>Lorem ipsum dolor sit amet, consectetur sed do adipiscing elit, sed do eiusmod tempor labore incididunt ut labore et dolore magna aliqua.</p></div>
</div>
<div class="feature" style="top:1747px">
  <svg class="hex" viewBox="0 0 66 72"><path d="M33 2 63 19v34L33 70 3 53V19Z" fill="var(--red)"/><circle cx="33" cy="30" r="7" fill="#fff"/><path d="M20 50c0-8 6-12 13-12s13 4 13 12z" fill="#fff"/></svg>
  <div><h4>Global Expertise</h4><p>Lorem ipsum dolor sit amet, consectetur sed do adipiscing elit, sed do eiusmod tempor labore incididunt ut labore et dolore magna aliqua.</p></div>
</div>

<!-- services -->
<div class="abs center kicker" style="top:1973px">Our Services</div>
<h2 class="abs center h2" style="top:1995px">What We <span>Offer</span></h2>
<div class="card featured" style="left:184px" role="img" aria-label="Non Polluting service with factory landscape photo">
  <svg width="60" height="52" viewBox="0 0 60 52"><path d="M4 48V26l12 8V26l12 8V26l12 8V8h12v40z" fill="none" stroke="var(--red)" stroke-width="3"/></svg>Non Polluting</div>
<div class="card" style="left:397px">
  <svg width="60" height="52" viewBox="0 0 60 52" fill="none" stroke="#333" stroke-width="2"><circle cx="32" cy="20" r="12"/><path d="M34 12l-5 9h6l-4 8" stroke="var(--red)"/><path d="M4 40c10-4 18 4 30 0l16-8"/></svg>Demand Respond</div>
<div class="card" style="left:611px">
  <svg width="60" height="52" viewBox="0 0 60 52" fill="none" stroke="var(--red)" stroke-width="2"><circle cx="30" cy="8" r="5"/><circle cx="30" cy="30" r="6"/><circle cx="14" cy="44" r="5"/><circle cx="46" cy="44" r="5"/><path d="M30 13v11M25 34l-7 6M35 34l7 6"/></svg>Load Shifting</div>
<div class="card" style="left:825px">
  <svg width="60" height="52" viewBox="0 0 60 52" fill="none" stroke="#333" stroke-width="2"><path d="M10 26a20 20 0 0 1 34-14M50 26a20 20 0 0 1-34 14"/><rect x="24" y="16" width="12" height="20" rx="2" stroke="var(--red)"/><path d="M28 13h4"/></svg>Renewable</div>
<div class="btn" style="left:523px;top:2294px;width:155px;height:40px;font-size:11px">View More Services</div>

<!-- projects -->
<section class="abs projects" style="background:var(--dark)"></section>
<svg class="abs" style="left:0;top:2900px" width="1200" height="100" viewBox="0 0 1200 100"><path d="M0 0H1200V30Q700 80 0 60Z" fill="var(--dark)"/><path d="M0 60Q700 80 1200 30V58Q700 95 0 60Z" fill="var(--red)"/><path d="M0 60Q700 95 1200 58V100H0Z" fill="#fff"/></svg>
<div class="abs proj-vert">PROJECTS</div>
<div class="abs proj-photo" role="img" aria-label="Hand checking terminals on a car battery"></div>
<div class="abs badge"><b>25</b><small>YEAR</small><div>Experience</div></div>
<div class="dot" style="left:172px;top:2647px;background:var(--red)"><svg width="10" height="10" viewBox="0 0 10 10"><path d="M7 1 3 5l4 4" stroke="#fff" stroke-width="1.6" fill="none"/></svg></div>
<div class="dot" style="left:518px;top:2647px;background:#2d2d2d;border:1px solid #555"><svg width="10" height="10" viewBox="0 0 10 10"><path d="m3 1 4 4-4 4" stroke="#fff" stroke-width="1.6" fill="none"/></svg></div>
<div class="abs proj-text" style="left:612px;top:2505px;width:405px">
  <h2 class="h2" style="color:#fff;margin-bottom:18px">Our Recent<br><span>Case Studies</span></h2>
  <p>Lorem ipsum dolor sit amet, consectetur adipisicing elit, sed do quis eiusmod tempor incididunt ut labore et dolore magna aliqua. Ut enim ad minim veniam, quis nostrud exercitation ullamco laboris nisi ut do aliquip ex ea commodo consequat. Duis aute irure dolor in voluptate reprehenderit in voluptate velit esse cillum dolore eu fugiat nulla pariatur. Excepteur sint occaecat cupidatat non proident, sunt in culpa qui officia deserunt mollit anim id est laborum.</p>
  <p>Lorem ipsum dolor sit amet, consectetur adipisicing elit, sed do quis eiusmod tempor incididunt ut labore et dolore magna aliqua. Ut enim ad minim veniam, quis nostrud exercitation ullamco laboris nisi ut do aliquip ex ea commodo consequat. Duis aute irure</p>
</div>

<!-- testimonials -->
<div class="abs center kicker" style="top:3055px">Testimonials</div>
<h2 class="abs center h2" style="top:3078px">What Client <span>Says</span></h2>
<div class="tcard" style="left:184px;width:260px;height:268px">
  <div class="quote">“</div><div class="stars">★★★★☆</div>
  <p>Lorem ipsum dolor sit amet, consectetur elit, sed do eiusmod tempor incididunt dolore magna aliqua. Quis ipsum su ultrices gravida. Risus commodo viv san lacus vel facilisis.</p>
  <h5>MAREK TOLSEN</h5><small>Graphic Designer</small></div>
<div class="tcard" style="left:768px;width:248px;height:268px">
  <div class="quote" style="left:-60px;color:transparent">“</div><div class="stars" style="margin-left:0">★★★★☆</div>
  <p>dolor sit amet, consectetur adipiscing eiusmod tempor incididunt ut labore et gna aliqua. Quis ipsum suspendisse avida. Risus commodo viverra maec san lacus vel facilisis.</p>
  <h5>MAREK TOLSEN</h5><small>Graphic Designer</small></div>
<div class="tcard mid" style="left:428px;top:3148px;width:342px;height:272px;box-shadow:0 6px 26px rgba(0,0,0,.1)">
  <div class="quote">“</div><div class="stars">★★★★☆</div>
  <p>Lorem ipsum dolor sit amet, consectetur adipiscing elit, sed do eiusmod tempor incididunt ut labore et dolore magna aliqua. Quis ipsum suspendisse ultrices gravida. Risus commodo viverra maec san lacus vel facilisis.</p>
  <h5>MAREK TOLSEN</h5><small>Graphic Designer</small></div>
<div class="dot" style="left:129px;top:3268px;background:var(--red)"><svg width="10" height="10" viewBox="0 0 10 10"><path d="M7 1 3 5l4 4" stroke="#fff" stroke-width="1.6" fill="none"/></svg></div>
<div class="dot" style="left:1036px;top:3268px;background:var(--black)"><svg width="10" height="10" viewBox="0 0 10 10"><path d="m3 1 4 4-4 4" stroke="#fff" stroke-width="1.6" fill="none"/></svg></div>

<!-- cta -->
<section class="abs cta" role="img" aria-label="Wind turbines at dusk over red hills">
  <h2 class="abs center" style="top:70px">GIVE US A CHANCE TO MAKE<br><span>US A DIIFFERENCE</span></h2>
  <p class="abs" style="left:335px;top:152px;width:530px;text-align:center;font-size:12.5px;line-height:21px;color:#eee">Lorem ipsum dolor sit amet, consectetur adipiscing elit, sed do eiusmod tempor incididunt ut labore et dolore magna aliqua. Quis ipsum suspendisse ultrices gravida. Risus commodo viverra maecenas accumsan lacus vel facilisis.</p>
  <div class="btn" style="left:528px;top:237px;width:145px;height:38px;font-size:11px">Contact Us Now</div>
</section>
<svg class="abs" style="left:0;top:3790px" width="1200" height="46" viewBox="0 0 1200 46"><path d="M0 46Q600 -10 1200 46Z" fill="#fff"/></svg>

<!-- footer -->
<footer>
  <div class="abs brand" style="left:184px;top:3890px;font-size:24px">ORVANE<br>TECHNOLOGY</div>
  <div class="abs" style="left:184px;top:3955px;width:232px;height:38px;background:var(--light);display:flex;align-items:center;font-size:12px;color:#999;padding-left:14px">
    <svg width="12" height="10" viewBox="0 0 12 10" style="margin-right:8px"><rect x=".5" y=".5" width="11" height="9" fill="none" stroke="#999"/><path d="m1 1 5 4 5-4" stroke="#999" fill="none"/></svg>Email Address
    <span style="position:absolute;right:0;top:0;width:40px;height:38px;background:var(--red);display:flex;align-items:center;justify-content:center"><svg width="14" height="14" viewBox="0 0 14 14"><path d="M1 7 13 1 9 13 7 8z" fill="#fff"/></svg></span>
  </div>
  <div class="social" style="left:184px"></div>
  <div class="social" style="left:225px"></div>
  <div class="social" style="left:267px"></div>
  <div class="abs footer-col" style="left:580px;top:3887px">
    <h6>QUICK LINKS</h6>
    <ul><li>Home</li><li>About Us</li><li>Services</li><li>Blog</li><li>Contact Us</li></ul>
  </div>
  <div class="abs footer-col" style="left:824px;top:3887px;width:200px">
    <h6>CONTACT US</h6>
    <div class="contact-row"><svg width="12" height="14" viewBox="0 0 12 14"><path d="M6 0a5 5 0 0 0-5 5c0 4 5 9 5 9s5-5 5-9a5 5 0 0 0-5-5z" fill="#222"/><circle cx="6" cy="5" r="2" fill="#fff"/></svg><div>Address:<br>Lorem Ipsum Dummy Text</div></div>
    <div class="contact-row"><svg width="12" height="12" viewBox="0 0 24 24"><path fill="#222" d="M6.6 10.8a15 15 0 0 0 6.6 6.6l2.2-2.2a1 1 0 0 1 1-.25 11.4 11.4 0 0 0 3.6.57 1 1 0 0 1 1 1V20a1 1 0 0 1-1 1A17 17 0 0 1 3 4a1 1 0 0 1 1-1h3.5a1 1 0 0 1 1 1c0 1.25.2 2.45.57 3.57a1 1 0 0 1-.25 1z"/></svg><div>Call Us:<br>555-014-2738</div></div>
    <div class="contact-row"><svg width="12" height="10" viewBox="0 0 12 10"><rect width="12" height="10" fill="#222"/><path d="m1 1 5 4 5-4" stroke="#fff" fill="none"/></svg><div>Email:<br>hello@orvanetech.com</div></div>
  </div>
  <div class="abs center" style="top:4110px;font-size:11.5px;color:#888">Copyright © 2021 <span style="color:var(--red)">Orvane Technology</span>. All Rights Reserved.</div>
</footer>

</body>
</html>
```